Business Card Design Project

We need a business card design for a new company focused on educational technology called 'Bright Harbor Educational Consulting'. We are a consulting company that helps other technology companies and schools market their solutions.

The final design should communicate the positive future of education, which is digital.

Industry/Entity Type

Business

Requirements
Nice to have
• four color, front and back.

```html
<!DOCTYPE html>
<html lang="en">
<head>
<meta charset="utf-8">
<title>Bright Harbor Educational Consulting – Business Cards</title>
<link href="https://fonts.googleapis.com/css2?family=Open+Sans:wght@400;600&display=swap" rel="stylesheet">
<style>
  :root {
    --bg: #e9e9ea;
    --blue-light: #5ea6e3;
    --blue-deep: #2b6fc0;
    --silver-light: #f4f4f5;
    --silver-dark: #b9bcc0;
    --ink: #2a2f3a;
    --navy: #1f3a68;
    --orange: #f08a1c;
    --green: #5fb52e;
    --purple: #4b3c9a;
    --red: #c8302b;
    --white: #ffffff;
  }
  html, body {
    margin: 0;
    width: 1200px;
    height: 951px;
    overflow: hidden;
    background: var(--bg);
    font-family: "Open Sans", Arial, sans-serif;
  }
  .canvas { position: relative; width: 1200px; height: 951px; }

  .card {
    position: absolute;
    width: 620px;
    height: 360px;
    border-radius: 22px;
    overflow: hidden;
    box-shadow: 0 10px 28px rgba(0,0,0,.18);
  }

  /* Front */
  .card-front {
    left: 90px; top: 70px;
    background: radial-gradient(circle at 45% 30%, var(--blue-light), var(--blue-deep) 75%);
  }
  .brand-panel {
    position: absolute;
    left: 160px; top: 0;
    width: 300px; height: 250px;
    border-radius: 0 0 22px 22px;
    background: linear-gradient(135deg, var(--silver-light), var(--silver-dark));
    display: flex; align-items: center; justify-content: center;
  }
  .brand {
    display: flex; align-items: center; gap: 12px;
    color: var(--navy); font-weight: 600;
  }
  .brand-mark { width: 22px; height: 22px; background: var(--navy); flex: none; }
  .brand-name { font-size: 22px; line-height: 1.15; text-transform: uppercase; }
  .brand-name small { display: block; font-size: 11px; letter-spacing: 3px; }
  .front-url {
    position: absolute; left: 0; right: 0; top: 285px;
    text-align: center; color: var(--white);
    font-size: 19px; letter-spacing: 2px;
  }

  /* Back */
  .card-back {
    left: 490px; top: 510px;
    background: linear-gradient(160deg, var(--white), #f1f1f2);
  }
  .card-back .brand { position: absolute; left: 150px; top: 50px; }
  .card-back .brand-name { font-size: 26px; }
  .card-back .brand-name small { font-size: 12px; letter-spacing: 4px; }

  .address {
    position: absolute; left: 30px; top: 185px;
    font-size: 17px; line-height: 1.25; color: var(--ink);
  }
  .address .line { display: flex; align-items: center; gap: 8px; }
  .address .indent { padding-left: 22px; }

  .contact {
    position: absolute; right: 32px; top: 170px;
    text-align: right; color: var(--ink);
  }
  .person-name { font-size: 24px; color: var(--orange); }
  .person-role { font-size: 15px; color: var(--green); margin-bottom: 14px; }
  .contact .line { display: flex; justify-content: flex-end; align-items: center; gap: 8px; font-size: 17px; line-height: 1.2; }

  .icon { width: 14px; height: 14px; flex: none; }

  .stripe-bar {
    position: absolute; left: 0; bottom: 0; width: 100%; height: 44px;
  }
  .back-url {
    position: absolute; right: 20px; bottom: 10px;
    font-size: 16px; color: var(--ink);
  }
  .back-url span { color: var(--green); }
</style>
</head>
<body>
<div class="canvas">

  <section class="card card-front" aria-label="Business card front">
    <div class="brand-panel">
      <div class="brand">
        <div class="brand-mark"></div>
        <div class="brand-name">Bright Harbor<small>Educational Consulting</small></div>
      </div>
    </div>
    <p class="front-url" style="margin:0">www.brightharboredu.com</p>
  </section>

  <section class="card card-back" aria-label="Business card back">
    <div class="brand">
      <div class="brand-mark"></div>
      <div class="brand-name">Bright Harbor<small>Educational Consulting</small></div>
    </div>

    <div class="address">
      <div class="line">
        <svg class="icon" viewBox="0 0 14 14"><path d="M7 1 L13 7 H11 V13 H3 V7 H1 Z" fill="var(--orange)"/></svg>
        P.O Box 482
      </div>
      <div class="indent">Maple Ridge</div>
      <div class="indent">Oregon 97000-0482</div>
    </div>

    <div class="contact">
      <div class="person-name">Maya Lindqvist</div>
      <div class="person-role">director</div>
      <div class="line">555 214 7630
        <svg class="icon" viewBox="0 0 14 14"><path d="M3 1 L6 1 L7 4 L5 5.5 Q6.5 8.5 8.5 9 L10 7 L13 8 L13 11 Q13 13 10 13 Q2 11 1 3 Q1 1 3 1Z" fill="var(--orange)"/></svg>
      </div>
      <div class="line">555 214 7631
        <svg class="icon" viewBox="0 0 14 14"><rect x="1" y="5" width="12" height="7" rx="1" fill="var(--orange)"/><rect x="4" y="1" width="6" height="5" fill="var(--orange)"/></svg>
      </div>
      <div class="line">brightharboredu.com
        <svg class="icon" viewBox="0 0 14 14"><rect x="1" y="3" width="12" height="9" rx="1" fill="var(--orange)"/><path d="M1 3 L7 8 L13 3" stroke="var(--white)" fill="none"/></svg>
      </div>
    </div>

    <svg class="stripe-bar" viewBox="0 0 620 44" preserveAspectRatio="none">
      <polygon points="0,10 70,10 50,44 0,44" fill="var(--purple)"/>
      <polygon points="70,10 190,10 170,44 50,44" fill="var(--green)"/>
      <polygon points="190,10 300,10 280,44 170,44" fill="var(--orange)"/>
      <polygon points="300,10 410,10 390,44 280,44" fill="var(--red)"/>
      <polygon points="410,10 620,10 620,44 390,44" fill="#dadbdd"/>
    </svg>
    <div class="back-url">www.<span>brightharboredu</span>.com</div>
  </section>

</div>
</body>
</html>
```